Popup Nightclub Grand Opening Flyer

We need to design a flyer for the grand opening of an upscale, exclusive nightclub called "Lanternfall". The design needs to be chic and exclusive. The background should be black and the text should primarily be white. We like minimalist designs.

Here is the text for the flyer
-
Velvetrope Atlanta Presents

Lanternfall (LOGO)

A Popup Nightclub Experience
For one night Only

Friday, October 18, 2013
Party begins at 9PM

INVITE ONLY

See invitation for location details
(Velvetrope Atlanta logo)

-
Examples we like

http://cdn2-b.brivelpost.com/sites/default/files/styles/image_content_width/hash/3d/fa/1472093815_4471_flyer.jpg?itok=R8kqWm2z

http://api.plovra.com/files/7Kqq-Tr82XXB3pQzJvmtR5HL2W719E4nbRtC6KLd4HsfM8Y2qTDK-VmjwDoNqLX4QBzTHD9nakRbVx3m-Pfq8htc3MDTWr5p4/2zelSaturdays.jpg

http://quenmar.com/wp-content/uploads/yootheme/widgetkit/gallery/2zel/2zel-gen_vroom4-01.jpg

Hi All, one thing that we are seeing that we don't like is on over emphasis on the phrase "a popup nightclub experience" please don't make this the largest thing on the flyer

Target Market(s)

Target market is 25-35 year olds who are affluent (rich) and like luxury brands

Requirements
Must have
• Dark Background
Nice to have
• Velvetrope Logo on the bottom
Modern text that isn't curvy
Should not have
• Curved text

```html
<!DOCTYPE html>
<html lang="en">
<head>
<meta charset="utf-8">
<title>Lanternfall – Popup Nightclub</title>
<link rel="stylesheet" href="https://fonts.googleapis.com/css2?family=Jost:wght@300;400;500;700&display=swap">
<style>
  :root {
    --ink: #e9f3ff;
    --glow: rgba(170, 215, 255, 0.75);
    --night: #050505;
    --aurora-green: #1f9c45;
    --aurora-green-deep: #0d4f22;
    --aurora-magenta: #9c1f78;
    --aurora-magenta-deep: #4a0d3a;
    --rule: rgba(233, 243, 255, 0.9);
  }
  html, body {
    margin: 0;
    padding: 0;
    width: 1200px;
    height: 1080px;
    overflow: hidden;
    background: var(--night);
  }
  .flyer {
    position: relative;
    width: 1200px;
    height: 1080px;
    overflow: hidden;
    font-family: "Jost", "Futura", sans-serif;
    color: var(--ink);
    text-transform: uppercase;
  }
  .aurora {
    position: absolute;
    inset: 0;
    background:
      radial-gradient(ellipse 70% 75% at 22% 100%, var(--aurora-green) 0%, var(--aurora-green-deep) 45%, transparent 80%),
      radial-gradient(ellipse 45% 70% at 100% 18%, var(--aurora-magenta) 0%, var(--aurora-magenta-deep) 50%, transparent 85%),
      linear-gradient(115deg, #0a1a0e 0%, var(--night) 45%, #140510 100%);
  }
  .line {
    position: absolute;
    left: 0;
    width: 1200px;
    text-align: center;
    line-height: 1;
    margin: 0;
    text-shadow: 0 0 10px var(--glow), 0 0 3px var(--glow);
  }
  .presenter { top: 58px; font-size: 26px; font-weight: 500; letter-spacing: 0.12em; }
  .brand-mark {
    position: absolute;
    left: 524px;
    top: 164px;
    width: 152px;
    height: 152px;
  }
  .brand-name {
    position: absolute;
    left: 0;
    width: 1200px;
    top: 340px;
    text-align: center;
    margin: 0;
    font-size: 64px;
    font-weight: 300;
    letter-spacing: 0.14em;
    line-height: 1;
    color: var(--ink);
  }
  .tagline { font-size: 39px; font-weight: 700; letter-spacing: 0.05em; }
  .tagline-1 { top: 514px; }
  .tagline-2 { top: 571px; }
  .divider {
    position: absolute;
    left: 348px;
    top: 626px;
    width: 504px;
    height: 2px;
    background: var(--rule);
    box-shadow: 0 0 6px var(--glow);
  }
  .date { top: 648px; font-size: 36px; font-weight: 300; letter-spacing: 0.03em; }
  .start-time { top: 696px; font-size: 36px; font-weight: 400; letter-spacing: 0.1em; }
  .access {
    position: absolute;
    left: 330px;
    top: 778px;
    width: 522px;
    display: flex;
    align-items: center;
    gap: 10px;
  }
  .access .rule-segment {
    flex: 1;
    height: 2px;
    background: var(--rule);
    box-shadow: 0 0 6px var(--glow);
  }
  .access .label {
    font-size: 36px;
    font-weight: 700;
    letter-spacing: 0.03em;
    line-height: 1;
    text-shadow: 0 0 10px var(--glow), 0 0 3px var(--glow);
  }
  .location-note { top: 875px; font-size: 22px; font-weight: 500; letter-spacing: 0.12em; }
  .host-sign {
    position: absolute;
    left: 0;
    width: 1200px;
    top: 946px;
    display: flex;
    justify-content: center;
    align-items: center;
    gap: 18px;
  }
  .host-sign .dot {
    width: 34px;
    height: 34px;
    border-radius: 50%;
    border: 2px solid var(--ink);
    box-sizing: border-box;
  }
  .host-sign .host-name {
    font-size: 40px;
    font-weight: 400;
    letter-spacing: 0.04em;
    line-height: 1;
    color: var(--ink);
  }
</style>
</head>
<body>
  <main class="flyer">
    <div class="aurora" role="img" aria-label="Diagonal light streaks in green and magenta fading into a black background"></div>

    <p class="line presenter">Velvetrope Atlanta Presents</p>

    <svg class="brand-mark" viewBox="0 0 152 152" aria-hidden="true">
      <circle cx="76" cy="76" r="70" fill="none" stroke="#e9f3ff" stroke-width="6"/>
    </svg>
    <h1 class="brand-name">Lanternfall</h1>

    <p class="line tagline tagline-1">A Popup Nightclub Experience</p>
    <p class="line tagline tagline-2">For One Night Only</p>

    <div class="divider"></div>

    <p class="line date">Friday, October 18, 2013</p>
    <p class="line start-time">Party Begins at 9PM</p>

    <div class="access">
      <span class="rule-segment"></span>
      <span class="label">Invite Only</span>
      <span class="rule-segment"></span>
    </div>

    <p class="line location-note">See Invitation for Location Details</p>

    <div class="host-sign">
      <span class="dot"></span>
      <span class="host-name">VELVETROPE</span>
    </div>
  </main>
</body>
</html>
```